依頼詳細
この度、胡蝶蘭に同梱させていただいている胡蝶蘭のお手入れ方法冊子をリニューアルし、お届け先もお客様にも見込み客になっていただけるような冊子を作りたいと思っています。

同梱物制作の際に参考にさせて頂いたサイトにイラストや漫画が有効とありましたので、そのように制作したいと考えております。 対象は目の良い10代や20代より、30代以上とご認識頂いて“見やすさ”“読みやすさ”を重視しております。

参照サイト
https://www.hanbai-kenkyu-lab.example/blog/offlinecrm/includedeitems_2points

また、コンペ方式ではございますので、ご提案は完成品ではなく一部イメージで良いです。当選確定後に完成作業をお願いいたします。
イラスト数
5点
希望イメージ
シンプル 複雑
単色 カラフル
暗い 明るい
日常 高級
遊び心 厳粛
未来的 伝統的
女性的 男性的
希望する色
赤系、黄・オレンジ系、緑系
納品ファイル
• 高解像度JPG (.jpg)
• イラストレーター形式 (.ai)
• フォトショップ形式 (.psd)
• PNG形式 (.png)
補足説明
添付指示書をご参照ください。
また、お気軽にご質問ください。
青葉ガーデン.comのURLです
https://www.aoba-garden.example/
①サイズについてーA4を二つ折りにしたA5 (148.5 x 210mm)を考えております
ただし、冊子作成ご依頼書にもありますようにコンテンツの内容によっては
複数ページになっても構いません。

②送付形態についてー透明なビニールケースにいれて胡蝶蘭に同梱しております。

```html
<!DOCTYPE html>
<html lang="ja">
<head>
<meta charset="utf-8">
<title>胡蝶蘭のお手入れ方法</title>
<link href="https://fonts.googleapis.com/css2?family=Klee+One:wght@400;600&display=swap" rel="stylesheet">
<style>
  :root {
    --paper: #fdfcf8;
    --ink: #4a4242;
    --muted: #8d8580;
    --petal-yellow: #f6e46a;
    --petal-orange: #f0a95a;
    --petal-pink: #f2a6bf;
    --stem-green: #a9c97c;
    --spark: #5a5252;
  }
  * { margin: 0; padding: 0; box-sizing: border-box; }
  html, body { width: 843px; height: 1200px; overflow: hidden; background: var(--paper); }
  .cover {
    position: relative;
    width: 843px;
    height: 1200px;
    background: var(--paper);
    font-family: "Klee One", sans-serif;
    color: var(--ink);
  }
  .art { position: absolute; }
  .orchid-spray {
    left: 270px; top: 0;
    width: 573px; height: 930px;
    border-radius: 48% 10% 40% 52%;
    background:
      radial-gradient(circle at 30% 28%, rgba(240,169,90,0.75) 0 18%, transparent 30%),
      radial-gradient(circle at 68% 18%, rgba(246,228,106,0.9) 0 20%, transparent 33%),
      radial-gradient(circle at 58% 60%, rgba(246,228,106,0.9) 0 20%, transparent 33%),
      radial-gradient(circle at 45% 45%, rgba(169,201,124,0.35) 0 30%, transparent 55%);
  }
  .butterfly { width: 70px; height: 55px; border-radius: 50%; }
  .butterfly--yellow { background: var(--petal-yellow); }
  .butterfly--orange { background: var(--petal-orange); opacity: .8; }
  .butterfly--pink { background: var(--petal-pink); opacity: .8; }
  .cherub {
    left: 120px; top: 1040px; width: 80px; height: 70px;
    border-radius: 50%;
    background: radial-gradient(circle, #fbe3ea 0 50%, var(--petal-pink) 100%);
  }
  .title {
    position: absolute;
    left: 50px; top: 330px;
    font-weight: 600;
    line-height: 1;
  }
  .title__main {
    display: flex; flex-direction: column;
    font-size: 110px; gap: 12px;
  }
  .title__particle {
    position: absolute; left: 90px; top: 400px;
    font-size: 62px;
  }
  .title__sub {
    position: absolute; left: 0; top: 570px;
    font-size: 72px; letter-spacing: 4px; white-space: nowrap;
  }
  .sparkle { position: absolute; }
  .contact {
    position: absolute; left: 278px; top: 1052px;
    font-size: 32px; letter-spacing: 2px;
  }
  .brand {
    position: absolute; left: 440px; top: 1128px;
    display: flex; align-items: center; gap: 10px;
    font-size: 38px; color: var(--muted);
  }
  .brand__dot {
    width: 30px; height: 30px; border-radius: 50%;
    background: var(--muted);
  }
</style>
</head>
<body>
<main class="cover">
  <div class="art orchid-spray" role="img" aria-label="Watercolour illustration of yellow and orange moth orchids on arching green stems"></div>
  <div class="art butterfly butterfly--yellow" style="left:88px;top:170px" role="img" aria-label="Small yellow butterfly illustration"></div>
  <div class="art butterfly butterfly--orange" style="left:715px;top:30px" role="img" aria-label="Small orange butterfly illustration"></div>
  <div class="art butterfly butterfly--pink" style="left:700px;top:390px" role="img" aria-label="Small pink butterfly illustration"></div>
  <div class="art butterfly butterfly--pink" style="left:395px;top:645px" role="img" aria-label="Small pink butterfly illustration"></div>
  <div class="art butterfly butterfly--orange" style="left:725px;top:725px" role="img" aria-label="Small orange butterfly illustration"></div>
  <div class="art cherub" role="img" aria-label="Small pink cherub character illustration"></div>

  <h1 class="title">
    <span class="title__main"><span>胡</span><span>蝶</span><span>蘭</span></span>
    <span class="title__particle">の</span>
    <span class="title__sub">お手入れ方法</span>
  </h1>

  <svg class="sparkle" style="left:28px;top:870px" width="30" height="30" viewBox="0 0 30 30" aria-hidden="true">
    <path d="M15 2 Q16 14 28 15 Q16 16 15 28 Q14 16 2 15 Q14 14 15 2Z" fill="var(--spark)"/>
  </svg>
  <svg class="sparkle" style="left:580px;top:955px" width="30" height="30" viewBox="0 0 30 30" aria-hidden="true">
    <path d="M15 2 Q16 14 28 15 Q16 16 15 28 Q14 16 2 15 Q14 14 15 2Z" fill="var(--spark)"/>
  </svg>

  <p class="contact">フリーダイヤル 0120-345-218</p>

  <div class="brand">
    <span class="brand__dot"></span>
    <span class="brand__name">青葉ガーデン.com</span>
  </div>
</main>
</body>
</html>
```